CD-/Plattencover für Tonträgerfirma
Zielgruppe
Wir sind eine Tonträgerfirma und bewegen uns im Low-Budget-Segment.
Aufgabenstellung
Für eine KLassik Serie benötigen wir 7 Cover, welche aber im Grundlayout immer gleich seinen sollten. Es soll eine erkenntliche Serie entstehen.
Das Thema lautet: Velvet Hour
Die Unterthemen lauten:
1. The Amber Lantern Gathering
2. The Velvet Hour Riverside Suites
3. The Velvet Hour Meadow Steps
4. The Velvet Hour Moonlit Whispers
5. The Copper Table Evenings
6. The Silver Curtain Soirée
7. The Northwind Orchestral Treasures
Wir benötigen nicht das komplette Artwork, sondern ein Frontcover
(12 x 12 cm + 2 cm Beschnitt wg. etwaiger Verschiebung der Positionierung
Fertigstellung (Aufziehen des Inlays und Labels) erfolgt später bei uns im Hause
Wir benötigen später offene psd-Dateien mit allen Ebenen
Wichtig: Schriften nicht gerastert ggfs. Schrift mitliefern

```html
<!DOCTYPE html>
<html lang="en">
<head>
<meta charset="utf-8">
<title>Velvet Hour – Cover Series</title>
<link href="https://fonts.googleapis.com/css2?family=Dancing+Script:wght@400;500&family=Lato:wght@400&display=swap" rel="stylesheet">
<style>
  :root {
    --page: #ffffff;
    --ink: #ffffff;
    --amber-a: #be1e22; --amber-b: #ee8a0a;
    --river-a: #e96b12; --river-b: #fde400;
    --meadow-a: #f6e000; --meadow-b: #108432;
    --moon-a: #14813a; --moon-b: #259fd8;
    --copper-a: #2399d8; --copper-b: #2a2573;
    --silver-a: #2c2270; --silver-b: #881a77;
    --north-a: #901b6f; --north-b: #b3161f;
  }
  * { margin: 0; padding: 0; box-sizing: border-box; }
  html, body { width: 849px; height: 1200px; overflow: hidden; background: var(--page); }
  .sheet { position: relative; width: 849px; height: 1200px; }

  .cover {
    position: absolute;
    width: 242px; height: 242px;
    color: var(--ink);
    box-shadow: 2px 2px 4px rgba(0,0,0,0.18);
    --s: 1;
  }
  .cover::before {
    content: "";
    position: absolute;
    inset: calc(4px * var(--s));
    border: 0.6px solid rgba(255,255,255,0.75);
  }
  .cover-series {
    position: absolute;
    left: 18%;
    top: calc(194px * var(--s));
    font-family: "Lato", sans-serif;
    font-size: calc(10px * var(--s));
    line-height: 1;
    white-space: nowrap;
  }
  .cover-title {
    position: absolute;
    left: 7.3%;
    top: calc(204px * var(--s));
    font-family: "Dancing Script", cursive;
    font-weight: 400;
    font-size: calc(23px * var(--s));
    line-height: 1;
    white-space: nowrap;
  }

  .cover--feature { left: 270px; top: 175px; width: 308px; height: 308px; --s: 1.2727; }

  .cover--amber   { background: linear-gradient(45deg, var(--amber-a), var(--amber-b)); }
  .cover--river   { background: linear-gradient(45deg, var(--river-a), var(--river-b)); }
  .cover--meadow  { background: linear-gradient(45deg, var(--meadow-a), var(--meadow-b)); }
  .cover--moon    { background: linear-gradient(45deg, var(--moon-a), var(--moon-b)); }
  .cover--copper  { background: linear-gradient(45deg, var(--copper-a), var(--copper-b)); }
  .cover--silver  { background: linear-gradient(45deg, var(--silver-a), var(--silver-b)); }
  .cover--north   { background: linear-gradient(45deg, var(--north-a), var(--north-b)); }

  .col-1 { left: 25px; } .col-2 { left: 303px; } .col-3 { left: 581px; }
  .row-1 { top: 575px; } .row-2 { top: 854px; }
  .cover--north .cover-title { font-size: 21px; }
</style>
</head>
<body>
<main class="sheet">
  <section class="cover cover--feature cover--amber">
    <p class="cover-series">The Amber</p>
    <h1 class="cover-title">Lantern Gathering</h1>
  </section>

  <section class="cover cover--river col-1 row-1">
    <p class="cover-series">The Velvet Hour</p>
    <h2 class="cover-title">Riverside Suites</h2>
  </section>
  <section class="cover cover--meadow col-2 row-1">
    <p class="cover-series">The Velvet Hour</p>
    <h2 class="cover-title">Meadow Steps</h2>
  </section>
  <section class="cover cover--moon col-3 row-1">
    <p class="cover-series">The Velvet Hour</p>
    <h2 class="cover-title">Moonlit Whispers</h2>
  </section>

  <section class="cover cover--copper col-1 row-2">
    <p class="cover-series">The Copper</p>
    <h2 class="cover-title">Table Evenings</h2>
  </section>
  <section class="cover cover--silver col-2 row-2">
    <p class="cover-series">The Silver</p>
    <h2 class="cover-title">Curtain Soirée</h2>
  </section>
  <section class="cover cover--north col-3 row-2">
    <p class="cover-series">The Northwind</p>
    <h2 class="cover-title">Orchestral Treasures</h2>
  </section>
</main>
</body>
</html>
```